Old boys day 2025

HARTLEY FALCONS V BROOKVALE BULLS SUNDAY 10TH AUGUST
THIS IS A FREE EVENT FOR NEST MEMBERS
THE NEST WOULD LIKE TO WELCOME ALL PAST PLAYERS,
COACHES, COMMITTEE, SPONSORS & SUPPORTERS TO OUR
ANNUAL FALCON DAY OF CELEBRATION.
JOIN US IN THE PADDOCK FOR A GREAT DAY OF LEAGUE ACTION
WATCHING OUR CURRENT CROP OF FALCONS. YOU CAN PURCHASE A TICKET AND OR JOIN THE NEST @ WWW.HARTLEYNEST.COM.AU
IF YOU JOIN THE NEST PRIOR TO THE EVENT OLD BOYS DAY IS FREE OF CHARGE, YOU STILL NEED TO
PURCHASE/REGISTER A TICKET ON THE EVENTS PAGE SO WE KNOW YOU ARE ATTENDING.
WE WILL BE HONOURING 6 PREMIERSHIP WINNING TEAMS THIS YEAR: 1935 1ST GRADE (90 YEARS), 1980 RESERVE GRADE (45 YEARS), 1985 1ST GRADE (40 YEARS), 1985 U18'S (40 YEARS), 2005 1ST GRADE (20 YEARS) & 2015 1ST GRADE (10 YEARS)
IN THE 1ST GRADE GAME THE PLAYERS WILL BE WEARING REPLICA 1985 JERSEYS (attached) WITH THE 85 PLAYERS NAMES ON THE BACK, THE NEST WILL BE HOSTING A POST GAME FUNCTION AT THE WREN GATE INN WHERE THESE JERSEYS WILL BE AUCTIONED OFF TO RAISE MONEY.
PURCHASE YOUR TICKET AT WWW.HARTLEYNEST.COM.AU/EVENTS

Target Market(s)

ex players

Requirements
Must have
• I NEED A A4 FLYER DESIGN & A DESIGN THAT WILL SUIT SOCIAL MEDIA

```html
<!DOCTYPE html>
<html lang="en">
<head>
<meta charset="utf-8">
<title>Hartley Falcons Old Boys Day Flyer</title>
<link href="https://fonts.googleapis.com/css2?family=Poppins:wght@300;400;500;600;700;800&family=Saira+Extra+Condensed:wght@700;800&display=swap" rel="stylesheet">
<style>
  :root {
    --green: #4db848;
    --green-dark: #1f6f2a;
    --green-deep: #0f3d17;
    --black: #141414;
    --charcoal: #232323;
    --white: #ffffff;
    --page: #c9c9c9;
    --body-font: "Poppins", sans-serif;
    --display-font: "Saira Extra Condensed", "Arial Narrow", "Roboto Condensed", sans-serif;
  }
  * { margin: 0; padding: 0; box-sizing: border-box; }
  html, body { width: 1200px; height: 2339px; overflow: hidden; }
  body { background: var(--page); font-family: var(--body-font); }

  .flyer {
    position: absolute; left: 30px; top: 374px;
    width: 1140px; height: 1590px; overflow: hidden;
    background: var(--green-dark);
    box-shadow: 0 20px 50px rgba(0,0,0,.35);
  }
  .flyer-bg { position: absolute; inset: 0; }
  .abs { position: absolute; }

  .club-badge {
    left: 62px; top: 66px; width: 218px; height: 260px;
    display: flex; flex-direction: column; align-items: center; justify-content: center; gap: 14px;
  }
  .club-badge .mark { width: 26px; height: 26px; background: var(--black); }
  .club-badge .name { font-weight: 800; font-size: 40px; color: var(--black); line-height: 1; text-align: center; }

  .free-event {
    left: 428px; top: 60px; font-weight: 800; font-size: 30px; color: var(--white); white-space: nowrap;
  }
  .free-event em { font-style: normal; color: var(--green); }
  .welcome {
    left: 428px; top: 108px; font-size: 24px; line-height: 31px; color: var(--white);
  }
  .welcome b { font-weight: 600; }

  .calendar-icon { left: 572px; top: 286px; width: 70px; height: 80px; }
  .event-date {
    left: 660px; top: 266px; width: 420px; overflow: hidden; font-family: var(--display-font); font-weight: 800;
    color: var(--white); line-height: .95; white-space: nowrap;
  }
  .event-date .day { font-size: 52px; letter-spacing: 24px; }
  .event-date .date { font-size: 56px; letter-spacing: 1px; }

  .match-title {
    left: 196px; top: 396px; width: 768px; height: 172px; overflow: hidden; text-align: center;
    font-family: var(--display-font); font-weight: 800; font-size: 88px; line-height: 86px;
    color: #ececec; letter-spacing: 1px; white-space: nowrap;
  }
  .versus {
    left: 562px; top: 466px; width: 34px; height: 34px; border-radius: 50%;
    background: var(--green); color: var(--black); font-weight: 700; font-size: 18px;
    display: flex; align-items: center; justify-content: center; border: 2px solid var(--black);
  }
  .home-club {
    left: 60px; top: 420px; width: 120px; height: 130px; text-align: center;
    display: flex; flex-direction: column; align-items: center; justify-content: center; gap: 8px;
  }
  .home-club .name, .away-club .name { font-weight: 700; font-size: 16px; color: var(--white); line-height: 1.15; }
  .home-club .mark, .away-club .mark { width: 16px; height: 16px; border-radius: 50%; background: var(--white); }
  .away-club {
    left: 978px; top: 430px; width: 140px; height: 110px; text-align: center;
    display: flex; flex-direction: column; align-items: center; justify-content: center; gap: 8px;
  }

  .join-us { left: 74px; top: 586px; font-weight: 700; font-size: 24px; color: var(--white); white-space: nowrap; }
  .join-us em { font-style: normal; color: var(--green); }

  .free-charge {
    left: 74px; top: 700px; font-weight: 600; font-size: 33px; line-height: 40px; color: var(--black);
  }
  .free-charge em { font-style: normal; color: var(--green); }
  .ticket-stamp {
    left: 74px; top: 827px; width: 176px; height: 82px;
    display: flex; flex-direction: column; align-items: center; justify-content: center;
    font-weight: 700; font-size: 21px; line-height: 22px; color: var(--green);
  }
  .ticket-stamp span:last-child { color: var(--white); }
  .register-note { left: 270px; top: 830px; font-size: 22px; line-height: 27px; color: var(--black); }

  .honours { left: 74px; top: 958px; color: var(--white); }
  .honours h2 { font-weight: 600; font-size: 26px; line-height: 36px; }
  .honours h2 em { font-style: normal; color: var(--green); }
  .honours ul { list-style: none; margin-top: 12px; }
  .honours li { font-size: 26px; line-height: 36px; padding-left: 24px; position: relative; }
  .honours li::before {
    content: ""; position: absolute; left: 2px; top: 13px; width: 9px; height: 9px;
    border-right: 2px solid var(--green); border-top: 2px solid var(--green); transform: rotate(45deg);
  }
  .honours li span { font-weight: 300; color: #cfcfcf; }

  .jersey-art {
    left: 800px; top: 718px; width: 240px; height: 300px;
    background: linear-gradient(180deg, #f4f4f4 0%, #d9d9d9 100%);
    clip-path: polygon(28% 0, 72% 0, 100% 14%, 94% 38%, 82% 34%, 82% 100%, 18% 100%, 18% 34%, 6% 38%, 0 14%);
  }
  .jersey-note {
    right: 60px; top: 1040px; width: 400px; text-align: right;
    font-size: 21px; line-height: 29px; color: var(--white);
  }
  .post-game {
    left: 628px; top: 1194px; width: 480px; font-size: 20px; line-height: 26px; color: var(--white);
  }

  .cta {
    left: 0; top: 1318px; width: 1140px; text-align: center;
    font-weight: 600; font-size: 33px; line-height: 40px; color: var(--white);
  }
  .site-pill {
    left: 302px; top: 1412px; width: 536px; height: 62px; border-radius: 31px;
    background: var(--white); display: flex; align-items: center; justify-content: center; gap: 14px;
    font-weight: 600; font-size: 27px; color: var(--green);
  }
  .site-pill svg { width: 30px; height: 30px; }
  .purchase-line {
    left: 0; top: 1512px; width: 1140px; text-align: center;
    font-weight: 600; font-size: 24px; color: var(--white);
  }
  .purchase-line em { font-style: normal; color: var(--green); }
</style>
</head>
<body>
<main class="flyer">
  <svg class="flyer-bg" viewBox="0 0 1140 1590" preserveAspectRatio="none" aria-hidden="true">
    <defs>
      <linearGradient id="stadium" x1="0" y1="0" x2="1" y2="1">
        <stop offset="0" stop-color="#2f9a3a"/>
        <stop offset=".5" stop-color="#1d6b27"/>
        <stop offset="1" stop-color="#0d3315"/>
      </linearGradient>
      <linearGradient id="greenBand" x1="0" y1="0" x2="1" y2="0">
        <stop offset="0" stop-color="#4db848"/>
        <stop offset="1" stop-color="#3fa63c"/>
      </linearGradient>
      <linearGradient id="footer" x1="0" y1="0" x2="0" y2="1">
        <stop offset="0" stop-color="#4db848"/>
        <stop offset="1" stop-color="#2b8a32"/>
      </linearGradient>
    </defs>
    <rect width="1140" height="1590" fill="url(#stadium)"/>
    <rect role="img" aria-label="Stadium crowd and floodlights photo in green tones" x="0" y="0" width="1140" height="580" fill="url(#stadium)" opacity=".6"/>
    <polygon points="0,0 360,0 0,390" fill="#fff"/>
    <polygon points="360,0 400,0 40,420 0,420 0,390" fill="#4db848" opacity=".7"/>
    <polygon points="400,52 1140,52 1140,100 360,100" fill="#141414"/>
    <polygon points="360,100 1140,100 1140,198 280,198" fill="url(#greenBand)"/>
    <polygon points="540,250 1140,250 1140,360 440,360" fill="#0f3d17" opacity=".6"/>
    <polygon points="560,262 1140,262 1140,370 460,370" fill="url(#greenBand)"/>
    <polygon points="0,370 1140,370 1140,572 0,572" fill="#0b2a10" opacity=".55"/>
    <polyline points="0,420 60,420 90,395 380,395" fill="none" stroke="#4db848" stroke-width="6"/>
    <polygon points="0,572 1000,572 960,634 0,634" fill="#141414"/>
    <polygon points="0,634 1140,634 1140,678 0,678" fill="#1a5222"/>
    <polygon points="0,678 780,678 620,912 0,912" fill="#fff"/>
    <line x1="0" y1="808" x2="700" y2="808" stroke="#4db848" stroke-width="3"/>
    <line x1="0" y1="908" x2="620" y2="908" stroke="#4db848" stroke-width="3"/>
    <polygon points="780,678 1140,650 1140,1040 560,1190 620,912" fill="#1f1f1f"/>
    <polygon points="1140,1040 560,1190 560,1290 1140,1290" fill="#2a8a33" opacity=".7"/>
    <polygon points="0,920 620,920 560,1290 0,1290" fill="#232323"/>
    <polygon points="560,1180 1140,1180 1140,1290 560,1290" fill="#141414"/>
    <rect x="0" y="1290" width="1140" height="300" fill="url(#footer)"/>
    <polygon points="0,1480 90,1420 1050,1420 1140,1480 1140,1590 0,1590" fill="#141414"/>
    <polyline points="0,1520 120,1440 1020,1440 1140,1520" fill="none" stroke="#4db848" stroke-width="4"/>
  </svg>

  <div class="abs club-badge">
    <span class="mark"></span>
    <span class="name">THE NEST</span>
  </div>

  <p class="abs free-event"><em>THIS IS A</em> FREE EVENT <em>FOR NEST MEMBERS</em></p>
  <p class="abs welcome">The NEST would like to Welcome all <b>Past Players,<br>Coaches, Committee, Sponsors &amp; Supporters</b> to<br>our annual falcon day of celebration.</p>

  <svg class="abs calendar-icon" viewBox="0 0 70 80" aria-hidden="true" fill="none" stroke="#141414" stroke-width="4">
    <rect x="4" y="10" width="56" height="54" rx="6"/>
    <line x1="18" y1="4" x2="18" y2="16"/><line x1="46" y1="4" x2="46" y2="16"/>
    <line x1="16" y1="30" x2="48" y2="30"/><line x1="16" y1="40" x2="48" y2="40"/><line x1="16" y1="50" x2="34" y2="50"/>
    <circle cx="50" cy="62" r="13" fill="#4db848"/>
    <polyline points="50,55 50,62 56,62"/>
  </svg>
  <div class="abs event-date">
    <div class="day">SUNDAY</div>
    <div class="date">10TH AUGUST</div>
  </div>

  <div class="abs home-club">
    <span class="mark"></span>
    <span class="name">HARTLEY<br>FALCONS</span>
  </div>
  <h1 class="abs match-title">HARTLEY FALCONS<br>BROOKVALE BULLS</h1>
  <div class="abs versus">V</div>
  <div class="abs away-club">
    <span class="mark"></span>
    <span class="name">BROOKVALE<br>BULLS</span>
  </div>

  <p class="abs join-us"><em>JOIN US</em> IN THE PADDOCK FOR A GREAT DAY OF LEAGUE ACTION</p>

  <p class="abs free-charge">If You <em>Join The Nest Prior</em> To The<br><em>Event Old Boys Day</em> Is Free Of Charge</p>
  <svg class="abs" style="left:74px;top:827px;width:176px;height:82px" viewBox="0 0 176 82" aria-hidden="true">
    <polygon points="10,0 166,0 176,12 166,24 176,41 166,58 176,70 166,82 10,82 0,70 10,58 0,41 10,24 0,12" fill="#141414"/>
    <rect x="14" y="8" width="148" height="66" fill="none" stroke="#4db848" stroke-width="2" stroke-dasharray="6 4"/>
  </svg>
  <div class="abs ticket-stamp"><span>PURCHASE</span><span>A TICKET</span></div>
  <p class="abs register-note">You Still Need To Purchase/Register<br>A Ticket On The Events Page<br>So We Know You Are Attending.</p>

  <section class="abs honours">
    <h2>We Will Be Honouring<br><em>6 Premiership Winning Teams</em> This Year:</h2>
    <ul>
      <li>1935 1st grade <span>(90 years)</span></li>
      <li>1980 reserve grade <span>(45 years)</span></li>
      <li>1985 1st grade <span>(40 years)</span></li>
      <li>1985 u18's <span>(40 years)</span></li>
      <li>2005 1st grade <span>(20 years)</span></li>
      <li>&amp; 2015 1st grade <span>(10 years)</span></li>
    </ul>
  </section>

  <div class="abs jersey-art" role="img" aria-label="Replica 1985 white jersey with black chevron and sponsor print"></div>
  <p class="abs jersey-note">In the 1st grade game the players will be wearing replica 1985 jerseys with the 85 players names on the back</p>
  <p class="abs post-game">The NEST will be hosting a post game function at the wren gate inn where these jerseys will be auctioned off to raise money.</p>

  <p class="abs cta">Watching Our Current Crop Of Falcons<br>You Can Purchase A Ticket And Or Join The Nest</p>
  <div class="abs site-pill">
    <svg viewBox="0 0 30 30" aria-hidden="true" fill="none" stroke="#141414" stroke-width="2">
      <circle cx="15" cy="15" r="12"/><ellipse cx="15" cy="15" rx="5" ry="12"/>
      <line x1="3" y1="15" x2="27" y2="15"/><line x1="5" y1="9" x2="25" y2="9"/><line x1="5" y1="21" x2="25" y2="21"/>
    </svg>
    WWW.HARTLEYNEST.COM.AU
  </div>
  <p class="abs purchase-line">PURCHASE YOUR TICKET AT <em>WWW.HARTLEYNEST.COM.AU/EVENTS</em></p>
</main>
</body>
</html>
```